Criação de Papelaria (6 itens) para Beleza
" REALIZANDO CIRURGIAS PLÁSTICAS EM PACIENTES QUE DESEJAM MELHORIAS NO CONTORNO CORPORAL OU EM ALGO QUE OS INCOMODE EM SUA APARÊNCIA "

```html
<!DOCTYPE html>
<html lang="pt-BR">
<head>
<meta charset="UTF-8">
<title>Rafael Moretti — Papelaria</title>
<link rel="stylesheet" href="https://fonts.googleapis.com/css2?family=Montserrat:wght@400;500&display=swap">
<style>
  :root {
    --stage: #e6e6e6;
    --paper: #ffffff;
    --ink: #3a3a3a;
    --ink-soft: #8a8a8a;
    --rule: #c9c9c9;
    --mark-light: #efefef;
    --mark-mid: #e2e2e2;
    --shadow: rgba(0,0,0,0.22);
  }
  * { box-sizing: border-box; margin: 0; padding: 0; }
  html, body { width: 1200px; height: 1200px; overflow: hidden; }
  body {
    background: var(--stage);
    font-family: "Montserrat", sans-serif;
    color: var(--ink);
    position: relative;
  }
  .sheet {
    position: absolute;
    background: var(--paper);
    box-shadow: 0 6px 18px var(--shadow);
    overflow: hidden;
  }
  .notepad   { left: 432px; top: 53px;  width: 396px; height: 523px; }
  .letterhead{ left: 233px; top: 600px; width: 367px; height: 492px; }
  .folder    { left: 612px; top: 600px; width: 372px; height: 492px; }

  .decor-circle {
    position: absolute;
    border-radius: 50%;
    background: radial-gradient(circle at 40% 40%, var(--mark-light), var(--mark-mid));
  }

  .brand { position: absolute; display: flex; align-items: center; gap: 8px; }
  .brand-dot { border-radius: 50%; background: var(--ink); flex: none; }
  .brand-text { display: flex; flex-direction: column; line-height: 1; }
  .brand-name { font-weight: 400; text-transform: uppercase; color: var(--ink); letter-spacing: 0.02em; }
  .brand-sub  { font-weight: 400; text-transform: uppercase; color: var(--ink); letter-spacing: 0.35em; margin-top: 3px; }

  .brand--small .brand-dot { width: 12px; height: 12px; }
  .brand--small .brand-name { font-size: 12px; }
  .brand--small .brand-sub  { font-size: 5px; }
  .brand--large .brand-dot { width: 22px; height: 22px; }
  .brand--large .brand-name { font-size: 21px; }
  .brand--large .brand-sub  { font-size: 8px; margin-top: 5px; }

  .date-field {
    position: absolute; right: 38px; top: 70px;
    width: 90px; border-bottom: 1px solid var(--ink);
    font-size: 10px; text-align: center; letter-spacing: 0.6em; padding-bottom: 1px;
  }
  .ruled-lines { position: absolute; left: 65px; right: 38px; top: 94px; }
  .ruled-lines span { display: block; height: 33px; border-bottom: 1px solid var(--rule); }

  .contact-bar {
    position: absolute; left: 0; right: 0;
    display: flex; justify-content: center; gap: 14px;
    font-size: 6px; color: var(--ink-soft); line-height: 1.3;
  }
  .contact-item { display: flex; align-items: center; gap: 4px; }
  .contact-item svg { width: 9px; height: 9px; flex: none; }
</style>
</head>
<body>

  <!-- Notepad -->
  <section class="sheet notepad">
    <div class="decor-circle" role="img" aria-label="Faint decorative brand shape" style="left:-70px; top:80px; width:260px; height:360px;"></div>
    <div class="brand brand--small" style="left:118px; top:24px;">
      <span class="brand-dot"></span>
      <span class="brand-text"><span class="brand-name">Rafael Moretti</span><span class="brand-sub">Cirurgia Plástica</span></span>
    </div>
    <div class="date-field">/ /</div>
    <div class="ruled-lines">
      <span></span><span></span><span></span><span></span><span></span><span></span>
      <span></span><span></span><span></span><span></span><span></span><span></span>
    </div>
    <footer class="contact-bar" style="bottom:20px;">
      <div class="contact-item"><svg viewBox="0 0 10 10"><circle cx="5" cy="5" r="5" fill="#8a8a8a"/></svg><span>(11) 4002-1234<br>(11) 9812-3456</span></div>
      <div class="contact-item"><svg viewBox="0 0 10 10"><circle cx="5" cy="5" r="5" fill="#8a8a8a"/></svg><span>R. das Flores, 120<br>Centro - Cidade</span></div>
      <div class="contact-item"><svg viewBox="0 0 10 10"><circle cx="5" cy="5" r="5" fill="#8a8a8a"/></svg><span>contato@rafaelmoretti.com</span></div>
      <div class="contact-item"><svg viewBox="0 0 10 10"><circle cx="5" cy="5" r="5" fill="#8a8a8a"/></svg><span>/rafaelmoretti</span></div>
    </footer>
  </section>

  <!-- Letterhead -->
  <section class="sheet letterhead">
    <div class="decor-circle" role="img" aria-label="Faint decorative brand shape" style="left:-80px; top:40px; width:270px; height:400px;"></div>
    <div class="brand brand--small" style="left:124px; top:430px;">
      <span class="brand-dot"></span>
      <span class="brand-text"><span class="brand-name">Rafael Moretti</span><span class="brand-sub">Cirurgia Plástica</span></span>
    </div>
    <footer class="contact-bar" style="bottom:12px;">
      <div class="contact-item"><svg viewBox="0 0 10 10"><circle cx="5" cy="5" r="5" fill="#8a8a8a"/></svg><span>(11) 4002-1234<br>(11) 9812-3456</span></div>
      <div class="contact-item"><svg viewBox="0 0 10 10"><circle cx="5" cy="5" r="5" fill="#8a8a8a"/></svg><span>R. das Flores, 120<br>Centro - Cidade</span></div>
      <div class="contact-item"><svg viewBox="0 0 10 10"><circle cx="5" cy="5" r="5" fill="#8a8a8a"/></svg><span>contato@rafaelmoretti.com</span></div>
      <div class="contact-item"><svg viewBox="0 0 10 10"><circle cx="5" cy="5" r="5" fill="#8a8a8a"/></svg><span>/rafaelmoretti</span></div>
    </footer>
  </section>

  <!-- Folder -->
  <section class="sheet folder">
    <div class="decor-circle" role="img" aria-label="Faint decorative brand shape" style="left:-70px; top:50px; width:240px; height:400px;"></div>
    <div class="brand brand--large" style="left:82px; top:246px;">
      <span class="brand-dot"></span>
      <span class="brand-text"><span class="brand-name">Rafael Moretti</span><span class="brand-sub">Cirurgia Plástica</span></span>
    </div>
  </section>

</body>
</html>
```